Leuchtkasten für Pflegedienst
Zielgruppe
Wir sind ein ambulnter Pflegedienst in Rostock. Derzeit befindet sich am Haus ein runder Leuchtkasten mit dem alten Logo. Das Logo wurde erneuert. Nun soll der Leuchtkasten mit einem Durchmessr von 80 cm neu gestaltet werden.
Aufgabenstellung
bitte zwei unterscheideliche Entwürfe für die Vorder und die Rückseite. Es sollte auf der einen Seite vielleicht das Logo anthalten sein und auf der anderen Seite eine andere kreative Idee. Hauskrankenpflege Sorgenhaus Linde sollten enthalten sein, sowie die Telefonummer 0381-52946138
Auf der anderen Seite wurde ein Schriftzug in Edelstahl rostoptik montiert.
Wichtig ist, dass das der ENtwurf auf einer durchleichtbaren Folie gedruckt werden kann.
Der KAffee slogan war füe eine andere Aktion und sollte nicht auf den Leuchtkasten.

```html
<!DOCTYPE html>
<html lang="de">
<head>
<meta charset="utf-8">
<title>Leuchtkasten Sorgenhaus Linde – Vorder- und Rückseite</title>
<link rel="stylesheet" href="https://fonts.googleapis.com/css2?family=Poppins:wght@600&display=swap">
<style>
  :root {
    --page-bg: #eceef1;
    --ring-blue: #2f63b3;
    --ring-blue-light: #4f8fd6;
    --brand-blue: #2a5aa8;
    --accent-blue: #4a9ad6;
    --navy: #26304f;
    --teal: #6fd1b4;
    --blush: #f6e2e8;
    --blush-deep: #e9b6c6;
    --white: #ffffff;
  }
  html, body {
    margin: 0;
    padding: 0;
    width: 840px;
    height: 1200px;
    overflow: hidden;
    background: var(--page-bg);
  }
  .sheet {
    width: 840px;
    height: 1200px;
    display: flex;
    flex-direction: column;
  }
  .lightbox-face {
    display: block;
    width: 840px;
    height: 600px;
  }
  .sign-text {
    font-family: "Poppins", sans-serif;
    font-weight: 600;
    letter-spacing: 2px;
    text-transform: uppercase;
  }
  .sign-text--blue { fill: var(--brand-blue); font-size: 34px; }
  .sign-text--navy { fill: var(--navy); font-size: 34px; }
  .brand-name {
    font-family: "Poppins", sans-serif;
    font-weight: 600;
  }
  .brand-name--center { fill: var(--brand-blue); font-size: 36px; }
  .brand-name--small { fill: var(--white); font-size: 19px; }
</style>
</head>
<body>
<main class="sheet">

  <!-- Vorderseite: Name und Leistung -->
  <svg class="lightbox-face lightbox-face--front" viewBox="0 0 840 600" aria-label="Vorderseite Leuchtkasten">
    <defs>
      <linearGradient id="front-ring" x1="0" y1="0" x2="1" y2="1">
        <stop offset="0" stop-color="var(--ring-blue-light)"/>
        <stop offset="1" stop-color="var(--ring-blue)"/>
      </linearGradient>
      <path id="front-top-arc" d="M 220,300 A 200,200 0 0 1 620,300"/>
      <path id="front-bottom-arc" d="M 198,300 A 222,222 0 0 0 642,300"/>
    </defs>
    <circle class="outer-ring" cx="420" cy="300" r="270" fill="url(#front-ring)"/>
    <circle class="face-disc" cx="420" cy="300" r="238" fill="var(--white)"/>

    <text class="sign-text sign-text--blue">
      <textPath href="#front-top-arc" startOffset="50%" text-anchor="middle">Sorgenhaus Linde</textPath>
    </text>
    <text class="sign-text sign-text--blue">
      <textPath href="#front-bottom-arc" startOffset="50%" text-anchor="middle">Hauskrankenpflege</textPath>
    </text>

    <path class="side-arc" d="M 218,226.5 A 215,215 0 0 0 212.3,355.6" fill="none" stroke="var(--brand-blue)" stroke-width="4" stroke-linecap="round"/>
    <path class="side-arc" d="M 622,226.5 A 215,215 0 0 1 627.7,355.6" fill="none" stroke="var(--brand-blue)" stroke-width="4" stroke-linecap="round"/>

    <circle class="inner-ring" cx="420" cy="300" r="150" fill="var(--white)" stroke="var(--accent-blue)" stroke-width="7"/>
    <text class="brand-name brand-name--center" x="420" y="290" text-anchor="middle">Sorgenhaus</text>
    <text class="brand-name brand-name--center" x="420" y="336" text-anchor="middle">Linde</text>
  </svg>

  <!-- Rückseite: Bildmotiv und Telefonnummer -->
  <svg class="lightbox-face lightbox-face--back" viewBox="0 0 840 600" aria-label="Rückseite Leuchtkasten">
    <defs>
      <clipPath id="back-window">
        <circle cx="420" cy="300" r="178"/>
      </clipPath>
      <radialGradient id="photo-tones" cx="0.5" cy="0.55" r="0.5">
        <stop offset="0" stop-color="var(--blush)"/>
        <stop offset="0.7" stop-color="var(--blush-deep)"/>
        <stop offset="0.92" stop-color="var(--blush-deep)" stop-opacity="0.6"/>
        <stop offset="1" stop-color="var(--blush-deep)" stop-opacity="0"/>
      </radialGradient>
      <path id="back-top-arc" d="M 215,300 A 205,205 0 0 1 625,300"/>
      <path id="back-bottom-arc" d="M 195,300 A 225,225 0 0 0 645,300"/>
    </defs>
    <circle class="face-disc" cx="420" cy="300" r="270" fill="var(--white)" stroke="var(--navy)" stroke-width="6"/>

    <text class="sign-text sign-text--navy">
      <textPath href="#back-top-arc" startOffset="55%" text-anchor="middle">Sorgenhaus Linde</textPath>
    </text>
    <text class="sign-text sign-text--navy">
      <textPath href="#back-bottom-arc" startOffset="50%" text-anchor="middle">0381-52946138</textPath>
    </text>

    <path class="side-arc" d="M 232,180 A 240,240 0 0 0 192,350" fill="none" stroke="var(--navy)" stroke-width="4" stroke-linecap="round"/>

    <g class="photo-window" clip-path="url(#back-window)">
      <rect x="240" y="120" width="360" height="360" fill="var(--navy)"/>
      <path class="teal-swoosh" d="M 240,255 C 330,300 430,350 600,395 L 600,480 L 240,480 Z" fill="var(--teal)"/>
      <ellipse class="photo-area" cx="440" cy="470" rx="200" ry="190" fill="url(#photo-tones)"
               role="img" aria-label="Foto: fröhlicher älterer Herr mit Brille zeigt die OK-Geste"/>
    </g>

    <circle class="brand-dot" cx="340" cy="218" r="7" fill="var(--white)"/>
    <text class="brand-name brand-name--small" x="354" y="225">Sorgenhaus Linde</text>
  </svg>

</main>
</body>
</html>
```